Piñalta farm website

We are a pineapple producer in the caribbean. Our local market is Spanish speaking. Our export market is English Speaking. Therefore we need let the user pick their language. We want a simple web site based upon the wordpress platform.

Regarding the home page we prefer a slideshow that scrolls our photos of the farm and produce. We have four key messages - high quality fruit, 12 months per year supply, fair labor practices, sustainable farming practices.

We contemplate a home page with 'about us' and 'gallery' and 'blog' menu options. 'about us' is a brief commentary as well as contact info and google map to our location. 'gallery' is additional photography that we can maintain via word press. 'blog' is just a blog.

local market is resorts and hotels and exporters to the USA and Europe

Farming

• wordpress platform

prefer natural colors - blue, green, brown, yellow - over radical colors.

```html
<!DOCTYPE html>
<html lang="en">
<head>
<meta charset="utf-8">
<title>Piñalta – Blog</title>
<link href="https://fonts.googleapis.com/css2?family=Arimo:wght@400;700&family=Noto+Serif:ital,wght@0,400;1,400&display=swap" rel="stylesheet">
<style>
  :root {
    --header-dark: #2f7d15;
    --header-mid: #3e9a1c;
    --hero-light: #5ccb38;
    --hero-mid: #45b02b;
    --hero-deep: #3a9d24;
    --tab-green: #4aa826;
    --crumb-band: #dedede;
    --soft-band: #f6f6f6;
    --white: #ffffff;
    --ink: #111111;
    --body-text: #7a7a7a;
    --meta-text: #a4a4a4;
    --rule: #e4e4e4;
    --sidebar-bg: #f0f1f0;
    --footer-dark: #1c1e1d;
    --photo-field: #7f9670;
    --photo-leaves: #a7b9a4;
  }
  * { box-sizing: border-box; margin: 0; padding: 0; }
  html, body { width: 1085px; height: 1200px; overflow: hidden; }
  body {
    position: relative;
    background: var(--white);
    font-family: "Arimo", Arial, sans-serif;
    color: var(--ink);
  }
  .site-header {
    position: absolute; left: 0; top: 0; width: 1085px; height: 78px;
    background: linear-gradient(180deg, var(--header-mid), var(--header-dark));
    border-bottom: 1px solid #6fcf46;
  }
  .brand {
    position: absolute; left: 58px; top: 24px; display: flex; align-items: center; gap: 10px;
    font-size: 30px; color: var(--white);
  }
  .brand-mark { width: 36px; height: 36px; background: #e0b640; border-radius: 4px; }
  .brand-divider { position: absolute; left: 264px; top: 12px; width: 1px; height: 56px; background: rgba(255,255,255,0.12); }
  .main-nav { position: absolute; left: 325px; top: 29px; display: flex; gap: 22px; }
  .main-nav a { color: var(--white); text-decoration: none; font-size: 15px; }
  .nav-pointer { position: absolute; left: 560px; top: 70px; }
  .lang-flags { position: absolute; left: 987px; top: 14px; display: flex; gap: 13px; }
  .search-tab {
    position: absolute; left: 974px; top: 52px; width: 89px; height: 27px;
    background: var(--tab-green); border-radius: 6px 6px 0 0;
    border: 1px solid #6fcf46; border-bottom: none;
    color: var(--white); font-size: 12px; padding: 6px 0 0 32px;
  }
  .search-tab svg { position: absolute; left: 13px; top: 8px; }
  .page-hero {
    position: absolute; left: 0; top: 79px; width: 1085px; height: 166px;
    background: linear-gradient(90deg, var(--hero-mid) 0%, var(--hero-light) 45%, var(--hero-mid) 75%, var(--hero-deep) 100%);
  }
  .page-hero h1 {
    position: absolute; left: 58px; top: 32px;
    font-family: "Noto Serif", Georgia, serif; font-weight: 400; font-size: 48px;
    color: var(--white); text-shadow: 0 1px 2px rgba(0,0,0,0.25);
  }
  .breadcrumb-band {
    position: absolute; left: 0; top: 245px; width: 1085px; height: 78px;
    background: var(--crumb-band); border-top: 1px solid #cfcfcf; border-bottom: 1px solid #cfcfcf;
    font-family: "Noto Serif", Georgia, serif; font-style: italic; font-size: 14px; color: #666;
    padding: 30px 0 0 58px;
  }
  .soft-band { position: absolute; left: 0; top: 323px; width: 1085px; height: 36px; background: var(--soft-band); }
  .post { position: absolute; left: 58px; width: 631px; }
  .post-title {
    font-family: "Noto Serif", Georgia, serif; font-weight: 400; font-size: 25px; height: 34px;
    border-bottom: 1px solid var(--rule);
  }
  .post-meta {
    height: 44px; border-bottom: 1px solid var(--rule);
    font-family: "Noto Serif", Georgia, serif; font-style: italic; font-size: 13px;
    text-transform: uppercase; color: var(--meta-text); padding-top: 13px;
  }
  .post-meta b { font-weight: 400; color: var(--ink); }
  .post-meta .sep { color: #ccc; }
  .post-thumb {
    position: absolute; left: -2px; top: 90px; width: 215px; height: 214px;
    border: 1px solid #d8d8d8; border-radius: 7px; padding: 7px; background: var(--white);
  }
  .post-thumb div { width: 100%; height: 100%; border-radius: 4px; }
  .post-excerpt {
    position: absolute; left: 235px; top: 97px; width: 375px;
    font-size: 13px; line-height: 26px; color: var(--body-text);
  }
  .read-more {
    position: absolute; left: 552px; top: 235px; width: 78px; height: 20px;
    border-radius: 10px; background: linear-gradient(#ffffff, #e3e3e3);
    box-shadow: 0 1px 2px rgba(0,0,0,0.45); font-size: 11px; color: var(--ink);
    text-align: center; line-height: 20px;
  }
  .sidebar {
    position: absolute; left: 754px; top: 367px; width: 275px; height: 256px;
    background: var(--sidebar-bg); border-radius: 0 0 6px 6px;
    box-shadow: 0 1px 2px rgba(0,0,0,0.15); padding: 22px 13px 0 13px;
  }
  .sidebar h2 {
    font-family: "Noto Serif", Georgia, serif; font-weight: 400; font-size: 19px;
    padding: 0 0 14px 13px; border-bottom: 1px solid #dcdcdc;
  }
  .recent-list { list-style: none; padding-top: 22px; }
  .recent-list li {
    display: flex; align-items: center; gap: 9px; height: 38px; padding-left: 12px;
    font-size: 13px; color: #666;
  }
  .site-footer {
    position: absolute; left: 0; top: 1125px; width: 1085px; height: 75px;
    background: linear-gradient(180deg, #2a2c2b, var(--footer-dark));
  }
</style>
</head>
<body>
  <header class="site-header">
    <div class="brand"><span class="brand-mark"></span>Piñalta</div>
    <span class="brand-divider"></span>
    <nav class="main-nav">
      <a href="#">Home</a><a href="#">About Us</a><a href="#">Gallery</a><a href="#">Blog</a>
    </nav>
    <svg class="nav-pointer" width="18" height="9" viewBox="0 0 18 9"><path d="M0 9 L9 0 L18 9 Z" fill="#5bc43a"/></svg>
    <div class="lang-flags">
      <svg width="17" height="12" viewBox="0 0 17 12" aria-label="Español">
        <rect width="17" height="12" fill="#c60b1e"/><rect y="3" width="17" height="6" fill="#ffc400"/>
      </svg>
      <svg width="17" height="12" viewBox="0 0 17 12" aria-label="English">
        <rect width="17" height="12" fill="#012169"/>
        <path d="M0 0 L17 12 M17 0 L0 12" stroke="#fff" stroke-width="2.4"/>
        <path d="M0 0 L17 12 M17 0 L0 12" stroke="#c8102e" stroke-width="0.9"/>
        <path d="M8.5 0 V12 M0 6 H17" stroke="#fff" stroke-width="3.6"/>
        <path d="M8.5 0 V12 M0 6 H17" stroke="#c8102e" stroke-width="2"/>
      </svg>
    </div>
    <div class="search-tab">
      <svg width="12" height="12" viewBox="0 0 12 12"><circle cx="7" cy="5" r="3.5" fill="none" stroke="#1a3d0c" stroke-width="1.6"/><path d="M4.5 7.5 L1 11" stroke="#1a3d0c" stroke-width="2"/></svg>
      search
    </div>
  </header>

  <section class="page-hero"><h1>Blog</h1></section>
  <div class="breadcrumb-band">Home » Blog</div>
  <div class="soft-band"></div>

  <article class="post" style="top:383px">
    <h2 class="post-title">Sustainable Farming Practices.</h2>
    <div class="post-meta">Posted by <b>root</b> on Apr 6, 2013 in <b>Slideshow</b> <span class="sep">|</span> <b>0 Comments</b></div>
    <div class="post-thumb"><div role="img" aria-label="Photo of rows of pineapple plants in a farm field" style="background:linear-gradient(180deg,#6f8a5c 0%,#9aa98a 30%,var(--photo-field) 100%)"></div></div>
    <p class="post-excerpt">This is an example page. It's different from a blog post because it will stay in one place and will show up in your site navigation (in most themes). Most people start with an About page that introduces them to potential site visitors. It might say something like this:</p>
    <span class="read-more">read more</span>
  </article>

  <article class="post" style="top:731px">
    <h2 class="post-title">Fair Labor Practices</h2>
    <div class="post-meta">Posted by <b>root</b> on Apr 6, 2013 in <b>Slideshow</b> <span class="sep">|</span> <b>0 Comments</b></div>
    <div class="post-thumb"><div role="img" aria-label="Photo of a farm worker among pineapple leaves" style="background:linear-gradient(135deg,#8fa58c,var(--photo-leaves) 60%,#96ab93)"></div></div>
    <p class="post-excerpt">This is an example page. It's different from a blog post because it will stay in one place and will show up in your site navigation (in most themes). Most people start with an About page that introduces them to potential site visitors. It might say something like this:</p>
    <span class="read-more">read more</span>
  </article>

  <aside class="sidebar">
    <h2>Recent Posts</h2>
    <ul class="recent-list">
      <li><svg width="10" height="12" viewBox="0 0 10 12"><rect x="0.5" y="0.5" width="9" height="11" fill="#fff" stroke="#bbb"/><path d="M2 3.5H8M2 6H8M2 8.5H8" stroke="#ccc"/></svg>Sustainable Farming Practices.</li>
      <li><svg width="10" height="12" viewBox="0 0 10 12"><rect x="0.5" y="0.5" width="9" height="11" fill="#fff" stroke="#bbb"/><path d="M2 3.5H8M2 6H8M2 8.5H8" stroke="#ccc"/></svg>Fair Labor Practices</li>
      <li><svg width="10" height="12" viewBox="0 0 10 12"><rect x="0.5" y="0.5" width="9" height="11" fill="#fff" stroke="#bbb"/><path d="M2 3.5H8M2 6H8M2 8.5H8" stroke="#ccc"/></svg>12 months per year supply</li>
      <li><svg width="10" height="12" viewBox="0 0 10 12"><rect x="0.5" y="0.5" width="9" height="11" fill="#fff" stroke="#bbb"/><path d="M2 3.5H8M2 6H8M2 8.5H8" stroke="#ccc"/></svg>High Quality Fruit</li>
    </ul>
  </aside>

  <footer class="site-footer"></footer>
</body>
</html>
```